" A clínica já existe há 15 anos, atendendo a classe "C". Já possui uma logo há 8 anos. Este serviço solicitado será para uma nova sede que atenderá o público "A". O produto principal desta nova clínica é o aparelho estético (invisível). "

```html
<!DOCTYPE html>
<html lang="pt-BR">
<head>
<meta charset="utf-8">
<title>Pasta de Documentos — Lucas Andrade Ortodontia Invisível</title>
<link rel="stylesheet" href="https://fonts.googleapis.com/css2?family=Montserrat:wght@300;400;500&display=swap">
<style>
  :root {
    --page: #ffffff;
    --board: #a9a9a9;
    --board-light: #d2d2d2;
    --ink: #111111;
    --cover-black: #0b0b0b;
    --cover-grey: #2a2a2a;
    --paper: #ffffff;
    --mark-grey: #4a4a4a;
    --soft-grey: #9a9a9a;
    --label: #1a1a1a;
  }
  * { margin: 0; padding: 0; box-sizing: border-box; }
  html, body { width: 1200px; height: 1200px; overflow: hidden; background: var(--page); }
  body { font-family: "Montserrat", Arial, sans-serif; position: relative; }

  .board {
    position: absolute; left: 12px; top: 76px; width: 1176px; height: 1064px;
    background: radial-gradient(ellipse at 50% 45%, var(--board-light) 0%, var(--board) 80%);
  }
  .board-title {
    position: absolute; left: 24px; top: 96px;
    font-size: 22px; font-weight: 500; letter-spacing: 0.5px; color: var(--label);
  }

  .folder { position: absolute; left: 140px; top: 180px; width: 916px; height: 880px; }

  .cover-back {
    position: absolute; left: 33px; top: 0; width: 441px; height: 583px;
    background: radial-gradient(ellipse at 70% 25%, var(--cover-grey) 0%, var(--cover-black) 60%);
    box-shadow: 0 4px 14px rgba(0,0,0,.35);
    color: #d8d8d8; text-align: center;
  }
  .cover-back .brand {
    position: absolute; left: 0; right: 0; top: 360px;
    display: flex; flex-direction: column; align-items: center; gap: 6px;
  }
  .brand-dot { width: 34px; height: 34px; border-radius: 50%; background: #8a8a8a; }
  .cover-back .brand-name { font-size: 17px; font-weight: 400; letter-spacing: 1px; color: #cfcfcf; }
  .cover-back .brand-tag { font-size: 8px; letter-spacing: 2px; color: #9a9a9a; text-transform: uppercase; }
  .contact { position: absolute; left: 0; right: 0; top: 468px; font-size: 9.5px; line-height: 19px; color: #cfcfcf; }

  .cover-front {
    position: absolute; left: 474px; top: 0; width: 442px; height: 583px;
    background: var(--paper);
    box-shadow: 0 4px 14px rgba(0,0,0,.3);
    text-align: center; overflow: hidden;
  }
  .cover-front .brand {
    position: absolute; left: 0; right: 0; top: 168px;
    display: flex; flex-direction: column; align-items: center;
  }
  .cover-front .brand-dot { width: 84px; height: 84px; background: var(--mark-grey); margin-bottom: 26px; }
  .cover-front .brand-name { font-size: 33px; font-weight: 400; color: var(--mark-grey); letter-spacing: 0.5px; }
  .brand-tagline {
    display: flex; align-items: center; gap: 8px; margin-top: 4px;
    font-size: 12.5px; letter-spacing: 3.5px; color: var(--mark-grey); text-transform: uppercase;
  }
  .brand-tagline::before, .brand-tagline::after { content: ""; width: 32px; height: 1px; background: var(--mark-grey); }
  .website {
    position: absolute; left: 0; right: 0; top: 455px;
    font-size: 11.5px; letter-spacing: 4px; color: var(--mark-grey);
  }
  .front-swoosh { position: absolute; left: 0; bottom: 0; width: 442px; height: 80px; }

  .pocket { position: absolute; left: 0; top: 583px; width: 474px; height: 300px; }
</style>
</head>
<body>
  <div class="board"></div>
  <h1 class="board-title">PASTA DE DOCUMENTOS</h1>

  <div class="folder">
    <section class="cover-back">
      <div class="brand">
        <span class="brand-dot"></span>
        <span class="brand-name">LUCAS ANDRADE</span>
        <span class="brand-tag">ortodontia invisível</span>
      </div>
      <p class="contact">
        (51) 3200.4100 &nbsp;|&nbsp; (51) 0000.0000 / 0000.0000<br>
        Rua das Acácias, 120-402 - Jardim Aurora - Porto Alegre RS
      </p>
    </section>

    <section class="cover-front">
      <div class="brand">
        <span class="brand-dot"></span>
        <span class="brand-name">LUCAS ANDRADE</span>
        <span class="brand-tagline">Ortodontia Invisível</span>
      </div>
      <p class="website">www.lucasandrade.com.br</p>
      <svg class="front-swoosh" viewBox="0 0 442 80" aria-hidden="true">
        <defs>
          <linearGradient id="swooshFill" x1="0" x2="1" y1="0" y2="0">
            <stop offset="0" stop-color="#000"/>
            <stop offset="0.6" stop-color="#1c1c1c"/>
            <stop offset="1" stop-color="#5a5a5a"/>
          </linearGradient>
        </defs>
        <path d="M0 52 C140 44 300 30 442 6 L442 80 L0 80 Z" fill="#bdbdbd"/>
        <path d="M0 60 C150 52 300 38 442 16 L442 80 L0 80 Z" fill="url(#swooshFill)"/>
        <path d="M0 57 C150 49 300 35 442 12" fill="none" stroke="#ffffff" stroke-width="1.5"/>
      </svg>
    </section>

    <svg class="pocket" viewBox="0 0 474 300" aria-hidden="true">
      <path d="M0 10 L33 0 L33 285 L0 290 Z" fill="#f2f2f2"/>
      <path d="M33 0 L474 0 L474 175 C380 180 300 200 230 250 C180 285 110 292 33 282 Z" fill="#0b0b0b"/>
      <path d="M33 0 L474 0 L474 40 C330 60 180 40 33 30 Z" fill="#1e1e1e" opacity=".6"/>
      <line x1="72" y1="140" x2="98" y2="168" stroke="#fff" stroke-width="3"/>
      <line x1="222" y1="60" x2="246" y2="90" stroke="#fff" stroke-width="3"/>
    </svg>
  </div>
</body>
</html>
```